Brightkoru NZ Brand, Revenue, Promotions & Events

I need an innovative business card that pops my brand. I like the colours against darker gradients and i'm not afraid to be bold.

I run my own Business, Brand, Event & Promotion company. I specialise in breathing life into businesses and adding atmosphere to promotions and events. I am concept based lady that likes to test the boundaries and create stand out campaigns that connect with the consumer.

I have 12 years business experience in a realm of interesting fields form 11 years in coordinating international music festivals & promotions, 6 years in radio with 8 radio awards including a NZ radio award for best sales team in NZ and was the national brand and sales manager for New Zealands 1st indoor entertainment mall. With 10 years of experience in advertising sales, I have an eye for creating revenue streams for businesses and thrive on implementing campaigns that compliment those streams.

I love sayings like "Do what you love, love what you do" and believe that you can achieve anything you want.

I have been fortunate in my career that my connections have carried me without needing to promote my business however it is important that I start to do so.

Target Market(s)

Decision makers 25 to 54

Contact Information for Business Card

Petra Holsworth
Director
p. 022 739 5081
e. petra@brightkoru.example
www.brightkoru.example

FB, IG and Linkedin logo

Font styles to use
Sans Serif

Colors

Designer to choose colors to be used in the design.

Requirements
Must have
• Petra Holsworth
• Director
• p. 022 739 5081
• e. petra@brightkoru.example
• www.brightkoru.example
• FB, IG and Linkedin logo
Nice to have
• I am looking for a business card with character, that leaves my presence with my customer and makes them remember my brand & optimistic personality when i walk out the door.

```html
<!DOCTYPE html>
<html lang="en">
<head>
<meta charset="utf-8">
<title>Brightkoru NZ – Business Card</title>
<link rel="stylesheet" href="https://fonts.googleapis.com/css2?family=Montserrat:wght@400;500;600&display=swap">
<style>
  :root {
    --bg: #e4e4e4;
    --card-white: #ffffff;
    --brand-blue: #29a9e1;
    --brand-blue-deep: #1b8cc4;
    --shade: #c9c9c9;
    --ink: #3a3a3a;
    --muted: #9a9a9a;
  }
  * { margin: 0; padding: 0; box-sizing: border-box; }
  html, body { width: 1200px; height: 800px; overflow: hidden; }
  body {
    background: var(--bg);
    font-family: "Montserrat", sans-serif;
    position: relative;
  }
  .card {
    position: absolute;
    top: 242px;
    width: 540px;
    height: 316px;
    border-radius: 26px;
    overflow: hidden;
  }
  .card--front { left: 40px; background: var(--card-white); }
  .card--back { left: 620px; background: var(--brand-blue); }

  .front__disc { position: absolute; left: 280px; top: -220px; width: 420px; height: 420px; }

  .social-row {
    position: absolute; right: 44px; top: 70px;
    display: flex; gap: 10px;
  }
  .social-dot {
    width: 24px; height: 24px; border-radius: 50%;
    background: var(--card-white);
  }

  .wordmark {
    position: absolute; left: 36px; top: 120px;
  }
  .wordmark__name {
    font-weight: 500; font-size: 23px; letter-spacing: 0.5px;
    color: var(--brand-blue); line-height: 1; text-transform: uppercase;
    display: flex; align-items: center; gap: 8px;
    white-space: nowrap;
  }
  .wordmark__dot {
    width: 12px; height: 12px; border-radius: 50%; background: var(--brand-blue);
  }
  .wordmark__tagline {
    margin-top: 6px; margin-left: 20px;
    font-size: 8.5px; letter-spacing: 0.5px; color: var(--muted);
    text-transform: uppercase; white-space: nowrap;
  }

  .person { position: absolute; left: 36px; top: 190px; }
  .person__name {
    font-weight: 500; font-size: 18px; letter-spacing: 0.5px;
    color: var(--brand-blue); text-transform: uppercase; line-height: 22px;
  }
  .person__role {
    font-size: 11px; letter-spacing: 1px; color: var(--muted);
    text-transform: uppercase; margin-top: 1px;
  }
  .contact { list-style: none; margin-top: 8px; }
  .contact__item {
    display: flex; align-items: center; gap: 8px;
    font-size: 12.5px; color: var(--ink); line-height: 18px;
  }
  .contact__icon { width: 11px; height: 11px; flex: none; }

  .back__wordmark {
    position: absolute; left: 0; right: 0; top: 120px; text-align: center;
  }
  .back__name {
    font-weight: 500; font-size: 48px; letter-spacing: 2px;
    color: var(--brand-blue-deep); text-transform: uppercase; line-height: 1;
  }
  .back__tagline {
    margin-top: 8px; font-size: 14px; letter-spacing: 1px;
    color: var(--brand-blue-deep); text-transform: uppercase;
  }
</style>
</head>
<body>

<section class="card card--front" aria-label="Business card front">
  <svg class="front__disc" viewBox="0 0 420 420" aria-hidden="true">
    <circle cx="202" cy="220" r="200" fill="var(--shade)"/>
    <circle cx="210" cy="210" r="200" fill="var(--brand-blue)"/>
  </svg>
  <div class="social-row" aria-label="Social media links">
    <span class="social-dot"></span>
    <span class="social-dot"></span>
    <span class="social-dot"></span>
  </div>

  <div class="wordmark">
    <div class="wordmark__name"><span class="wordmark__dot"></span>Brightkoru NZ</div>
    <div class="wordmark__tagline">Brand | Revenue | Events &amp; Promotions</div>
  </div>

  <div class="person">
    <div class="person__name">Petra Holsworth</div>
    <div class="person__role">Director</div>
    <ul class="contact">
      <li class="contact__item">
        <svg class="contact__icon" viewBox="0 0 24 24" aria-hidden="true"><path fill="var(--brand-blue)" d="M6.6 10.8a15.1 15.1 0 0 0 6.6 6.6l2.2-2.2a1 1 0 0 1 1-.25 11.4 11.4 0 0 0 3.6.57 1 1 0 0 1 1 1V20a1 1 0 0 1-1 1A17 17 0 0 1 3 4a1 1 0 0 1 1-1h3.5a1 1 0 0 1 1 1c0 1.25.2 2.45.57 3.57a1 1 0 0 1-.25 1z"/></svg>
        022 739 5081
      </li>
      <li class="contact__item">
        <svg class="contact__icon" viewBox="0 0 24 24" aria-hidden="true"><rect x="2" y="5" width="20" height="14" rx="2" fill="var(--brand-blue)"/><path d="M3 6l9 7 9-7" fill="none" stroke="#fff" stroke-width="2"/></svg>
        petra@brightkoru.example
      </li>
      <li class="contact__item">
        <svg class="contact__icon" viewBox="0 0 24 24" aria-hidden="true"><circle cx="12" cy="12" r="10" fill="var(--brand-blue)"/><path d="M2 12h20M12 2c3 3 3 17 0 20M12 2c-3 3-3 17 0 20" fill="none" stroke="#fff" stroke-width="1.5"/></svg>
        www.brightkoru.example
      </li>
    </ul>
  </div>
</section>

<section class="card card--back" aria-label="Business card back">
  <div class="back__wordmark">
    <div class="back__name">Brightkoru NZ</div>
    <div class="back__tagline">Brand | Revenue | Events &amp; Promotions</div>
  </div>
</section>

</body>
</html>
```